Building Custom Homes

We need a new business card design for a new company called " T & R Custom Homes" . We built custom homes according to our client's dream home. We would like to see designs that use the color blue, green, yellow, orange, pink depicting a home happy 'n bright!

Industry/Entity Type

Business

Contact Information for Business Card

Email: porvina73@quellmail.com.au Mobile: 0438 712 946 Phone: 02 6619 3874 Address: Shop 3 / 17 Wendover Lane Coffs Harbour, NSW 2450 Builders License Number : 47 18 3K ABN : 53 917 648 204 Name: Owen Padick

Colors
0355a3
0392cd
9bcb3c
e34297
f78f20
fbed22

Requirements
Must have
• The Company Name : "T & R Custom Homes"
• must depict the building industry

```html
<!DOCTYPE html>
<html lang="en">
<head>
<meta charset="utf-8">
<title>T &amp; R Custom Homes – Business Card</title>
<link rel="stylesheet" href="https://fonts.googleapis.com/css2?family=Bodoni+Moda:wght@400;500&display=swap">
<style>
  :root {
    --stage: #2a2a2c;
    --card-light: #e6e4e1;
    --card-mid: #d6d2cc;
    --brand-blue: #0355a3;
    --brand-green: #9bcb3c;
    --icon-yellow: #f5c23a;
    --icon-orange: #f78f20;
    --ink: #1f4f8f;
  }
  html, body {
    margin: 0;
    padding: 0;
    width: 1200px;
    height: 1000px;
    overflow: hidden;
    background: var(--stage);
  }
  .business-card {
    position: absolute;
    left: 75px;
    top: 200px;
    width: 1050px;
    height: 600px;
    background: radial-gradient(ellipse at 50% 45%, var(--card-light) 0%, var(--card-mid) 100%);
    box-shadow: 0 20px 50px rgba(0,0,0,0.5);
    overflow: hidden;
    font-family: "Bodoni Moda", "Didot", serif;
    color: var(--ink);
  }
  .brand {
    position: absolute;
    left: 250px;
    top: 70px;
    display: flex;
    align-items: center;
    gap: 22px;
  }
  .brand-mark {
    width: 54px;
    height: 54px;
    background: var(--brand-green);
  }
  .brand-name {
    font-size: 60px;
    font-weight: 500;
    color: var(--brand-blue);
    letter-spacing: 0.5px;
    white-space: nowrap;
  }
  .holder-name {
    position: absolute;
    left: 150px;
    top: 255px;
    font-size: 46px;
    font-weight: 500;
    color: var(--ink);
    margin: 0;
  }
  .divider {
    position: absolute;
    left: 560px;
    top: 235px;
    width: 2px;
    height: 240px;
    background: var(--brand-blue);
  }
  .contact-list {
    position: absolute;
    left: 592px;
    top: 238px;
    margin: 0;
    padding: 0;
    list-style: none;
    font-size: 19px;
    line-height: 1.3;
  }
  .contact-item {
    display: flex;
    align-items: flex-start;
    gap: 18px;
    margin-bottom: 20px;
  }
  .contact-icon {
    flex: 0 0 30px;
    width: 30px;
    height: 30px;
  }
  .card-band {
    position: absolute;
    left: 0;
    bottom: 0;
    width: 1050px;
    height: 60px;
  }
</style>
</head>
<body>
  <article class="business-card">
    <header class="brand">
      <span class="brand-mark"></span>
      <span class="brand-name">T &amp; R Custom Homes</span>
    </header>

    <h1 class="holder-name">Owen Padick</h1>

    <span class="divider"></span>

    <ul class="contact-list">
      <li class="contact-item">
        <svg class="contact-icon" viewBox="0 0 30 30" aria-hidden="true">
          <rect x="3" y="8" width="24" height="16" rx="2" fill="var(--icon-yellow)" stroke="var(--icon-orange)" stroke-width="1.5"/>
          <path d="M3 9 L15 18 L27 9" fill="none" stroke="var(--icon-orange)" stroke-width="1.5"/>
        </svg>
        <span>porvina73@quellmail.com.au</span>
      </li>
      <li class="contact-item">
        <svg class="contact-icon" viewBox="0 0 30 30" aria-hidden="true">
          <path d="M9 4 L13 9 L10 12 Q13 18 18 20 L21 17 L26 21 L23 26 Q12 26 4 10 Z" fill="var(--icon-yellow)" stroke="var(--icon-orange)" stroke-width="1.5"/>
        </svg>
        <span>02 6619 3874</span>
      </li>
      <li class="contact-item">
        <svg class="contact-icon" viewBox="0 0 30 30" aria-hidden="true">
          <path d="M3 15 L15 4 L27 15" fill="none" stroke="var(--brand-blue)" stroke-width="2.5"/>
          <rect x="7" y="14" width="16" height="12" fill="var(--icon-yellow)" stroke="var(--icon-orange)" stroke-width="1.5"/>
          <rect x="13" y="19" width="4" height="7" fill="var(--icon-orange)"/>
        </svg>
        <span>Shop 3 / 17 Wendover Lane Coffs Harbour,<br>NSW 2450</span>
      </li>
      <li class="contact-item">
        <svg class="contact-icon" viewBox="0 0 30 30" aria-hidden="true">
          <rect x="5" y="5" width="20" height="22" rx="2" fill="var(--icon-yellow)" stroke="var(--icon-orange)" stroke-width="1.5"/>
          <path d="M10 14 L14 18 L21 10" fill="none" stroke="var(--brand-blue)" stroke-width="2.5"/>
        </svg>
        <span>Builders License Number : 47 18 3K<br>ABN : 53 917 648 204</span>
      </li>
    </ul>

    <svg class="card-band" viewBox="0 0 1050 60" preserveAspectRatio="none" aria-hidden="true">
      <polygon points="0,24 598,24 610,60 0,60" fill="var(--brand-blue)"/>
      <polygon points="606,24 618,60 1050,60 1050,12 602,12" fill="var(--brand-green)"/>
      <polygon points="598,24 602,12 606,24 610,60 618,60 606,24" fill="var(--card-mid)"/>
    </svg>
  </article>
</body>
</html>
```